Cybersecurity company is looking for business card.

I need a business card design for our company, we are a cybersecurity company providing advance technology to protect agains any kind of malware. We need a fresh modern design it should communicate modern, technology and growth.

Target Market(s)

Business to business

Industry/Entity Type

Business

Contact Information for Business Card

Should have location, address, fax, mobile, phone, email and website.

Requirements
Must have
• Must follow company's logo color and style. Must have the company's log on its.

```html
<!DOCTYPE html>
<html lang="en">
<head>
<meta charset="utf-8">
<title>Vantrex Business Card</title>
<link href="https://fonts.googleapis.com/css2?family=Aldrich&display=swap" rel="stylesheet">
<style>
  :root {
    --backdrop: #e4e4e6;
    --card-white: #f7f7f7;
    --card-black: #0b0b0b;
    --accent-red: #b5121b;
    --ink-grey: #3a3a3a;
    --text-white: #ffffff;
  }
  html, body {
    margin: 0;
    width: 1200px;
    height: 900px;
    overflow: hidden;
    background: var(--backdrop);
  }
  .canvas {
    position: relative;
    width: 1200px;
    height: 900px;
  }
  .business-card {
    position: absolute;
    left: 100px;
    top: 164px;
    width: 1000px;
    height: 571px;
    border-radius: 60px;
    overflow: hidden;
    background: linear-gradient(160deg, #ffffff 0%, var(--card-white) 55%, #e9e9e9 100%);
    box-shadow: 0 18px 40px rgba(0,0,0,0.18);
    font-family: 'Aldrich', sans-serif;
  }
  .card-art {
    position: absolute;
    inset: 0;
  }
  .wave-black { fill: var(--card-black); }
  .stripe-red { fill: none; stroke: var(--accent-red); stroke-width: 12; }
  .stripe-black { fill: none; stroke: var(--card-black); stroke-width: 5; }
  .brand {
    position: absolute;
    left: 95px;
    top: 150px;
    display: flex;
    align-items: center;
    gap: 18px;
  }
  .brand-mark {
    width: 22px;
    height: 22px;
    background: var(--accent-red);
  }
  .brand-name {
    font-size: 104px;
    line-height: 1;
    color: var(--card-black);
    letter-spacing: -2px;
  }
  .person {
    position: absolute;
    left: 200px;
    top: 310px;
  }
  .person-name {
    font-size: 24px;
    color: var(--ink-grey);
    letter-spacing: 1px;
    text-transform: uppercase;
  }
  .person-role {
    font-size: 18px;
    color: var(--accent-red);
    margin-top: 2px;
    padding-left: 34px;
  }
  .address {
    position: absolute;
    left: 82px;
    top: 468px;
    font-size: 22px;
    line-height: 36px;
    color: var(--text-white);
  }
  .contact-list {
    position: absolute;
    right: 58px;
    top: 222px;
    margin: 0;
    padding: 0;
    list-style: none;
  }
  .contact-item {
    display: flex;
    justify-content: flex-end;
    align-items: center;
    gap: 12px;
    height: 40px;
    font-size: 20px;
    color: var(--text-white);
    letter-spacing: 1px;
  }
  .contact-icon {
    width: 22px;
    height: 22px;
    flex: none;
  }
  .contact-icon * { fill: none; stroke: var(--text-white); stroke-width: 2; }
  .contact-icon .solid { fill: var(--text-white); stroke: none; }
</style>
</head>
<body>
<div class="canvas">
  <div class="business-card">
    <svg class="card-art" viewBox="0 0 1000 571" preserveAspectRatio="none" aria-hidden="true">
      <path class="stripe-black" d="M0,318 C120,388 260,410 400,372 C560,282 720,98 1000,78"/>
      <path class="stripe-red" d="M0,350 C120,412 270,435 410,392 C565,304 720,120 1000,104"/>
      <path class="wave-black" d="M0,380 C120,440 260,460 400,420 C560,330 720,150 1000,130 L1000,571 L0,571 Z"/>
    </svg>

    <div class="brand">
      <span class="brand-mark"></span>
      <span class="brand-name">vantrex</span>
    </div>

    <div class="person">
      <div class="person-name">Marcus Hale</div>
      <div class="person-role">Managing Director</div>
    </div>

    <div class="address">
      047.12th floor,Plaza<br>
      Harbor Road KTM
    </div>

    <ul class="contact-list">
      <li class="contact-item">014 552 7310
        <svg class="contact-icon" viewBox="0 0 24 24"><path class="solid" d="M6.6 10.8a15 15 0 0 0 6.6 6.6l2.2-2.2a1 1 0 0 1 1-.25 11.4 11.4 0 0 0 3.6.57 1 1 0 0 1 1 1V20a1 1 0 0 1-1 1A17 17 0 0 1 3 4a1 1 0 0 1 1-1h3.5a1 1 0 0 1 1 1c0 1.25.2 2.45.57 3.570a1 1 0 0 1-.25 1z"/></svg>
      </li>
      <li class="contact-item">014 552 7311
        <svg class="contact-icon" viewBox="0 0 24 24"><rect x="7" y="2" width="10" height="20" rx="2"/><circle class="solid" cx="12" cy="18.5" r="1.2"/></svg>
      </li>
      <li class="contact-item">014 552 7312
        <svg class="contact-icon" viewBox="0 0 24 24"><rect x="4" y="9" width="16" height="11" rx="1"/><rect x="7" y="3" width="10" height="6"/><rect class="solid" x="7" y="13" width="3" height="2"/><rect class="solid" x="12" y="13" width="3" height="2"/></svg>
      </li>
      <li class="contact-item">info@vantrex.com
        <svg class="contact-icon" viewBox="0 0 24 24"><rect x="3" y="5" width="18" height="14"/><path d="M3 5l9 8 9-8"/></svg>
      </li>
      <li class="contact-item">www.vantrex.com
        <svg class="contact-icon" viewBox="0 0 24 24"><circle cx="12" cy="12" r="9"/><ellipse cx="12" cy="12" rx="4" ry="9"/><path d="M3 12h18M5 7h14M5 17h14"/></svg>
      </li>
    </ul>
  </div>
</div>
</body>
</html>
```